Website for Excavator and Earthworks Company

We require a modern, sleek and practical website for our newly created earthworks/excavator business in Perth, Western Australia called Gullwind Stonecut Earthworks.

The website should have a modern, cutting edge feel but only needs to be relatively simplistic in it's layout and eventual functionality.

Some pages it should have would be Home, About, Projects and Contact Us.

Number of Pages Required

1 page

```html
<!DOCTYPE html>
<html lang="en">
<head>
<meta charset="utf-8">
<title>Gullwind Stonecut Earthworks</title>
<link href="https://fonts.googleapis.com/css2?family=Krona+One&family=Montserrat:wght@400;500;600;700&display=swap" rel="stylesheet">
<style>
:root{
  --lime:#c9d32f;
  --orange:#d8951f;
  --dark:#1f1f1f;
  --ink:#111;
  --navy:#0f1d3a;
  --grey:#555;
  --light:#f2f2f2;
}
*{box-sizing:border-box;margin:0;padding:0}
html,body{width:1200px;height:3672px;overflow:hidden}
body{position:relative;background:#fff;font-family:"Montserrat",sans-serif;color:var(--ink)}
.abs{position:absolute}
.display{font-family:"Krona One",sans-serif;text-transform:uppercase;letter-spacing:1px}

/* header */
.topbar{left:385px;top:0;width:815px;height:31px;background:var(--lime);clip-path:polygon(26px 0,100% 0,100% 100%,0 100%)}
.topbar-info{left:460px;top:8px;font-size:13px;color:#333;display:flex;gap:36px}
.topbar-info b{font-weight:600;color:#111}
.brand{left:141px;top:28px;font-family:"Montserrat",sans-serif;font-weight:700;font-size:15px;color:var(--ink);display:flex;align-items:center;gap:8px}
.brand-mark{width:14px;height:14px;background:var(--lime)}
.nav{left:525px;top:53px;display:flex;gap:35px;font-size:13px;align-items:center}
.nav-cta{background:#000;color:#fff;padding:11px 17px}

/* hero */
.hero{left:0;top:92px;width:1200px;height:578px;background:linear-gradient(100deg,#ededed 0%,#dcdcdc 40%,#a99d82 70%,#7d6e57 100%)}
.hero-tag{left:141px;top:200px;background:#fff;padding:10px 18px;font-size:12px;font-weight:600}
.hero-title{left:141px;top:255px;font-size:42px;line-height:56px;color:#000}
.hero-text{left:141px;top:373px;border-left:4px solid var(--lime);padding-left:12px;font-size:16px;line-height:25px;font-weight:500;width:430px}
.btn{padding:14px 20px;font-size:14px;font-weight:500;display:flex;gap:10px;align-items:center}
.btn-lime{left:141px;top:490px;background:var(--lime)}
.btn-white{left:340px;top:490px;background:#fff}

/* about */
.about-img{left:0;top:770px;width:610px;height:344px;background:linear-gradient(135deg,#8f7a5a,#5f5a4c 50%,#b0a07a)}
.about-label{left:658px;top:735px;font-size:12px}
.about-title{left:658px;top:755px;font-size:25px;line-height:36px;color:var(--navy)}
.about-rule{left:658px;top:843px;width:118px;height:2px;background:var(--lime)}
.about-text{left:658px;top:862px;width:430px;font-size:12.5px;line-height:22px;color:#222}
.about-text p+p{margin-top:10px}
.btn-about{left:658px;top:1075px;background:var(--lime);font-size:12px;font-weight:700;padding:15px 15px}

/* services */
.services-intro{left:0;top:1198px;width:413px;height:600px;background:linear-gradient(160deg,#3a3a3a,#1d1d1d)}
.eyebrow{font-size:15px;color:var(--lime);display:flex;align-items:center;gap:8px}
.eyebrow::before{content:"";width:34px;height:1px;background:var(--lime)}
.eyebrow.center::after{content:"";width:34px;height:1px;background:var(--lime)}
.services-title{left:98px;top:1380px;font-size:30px;line-height:38px;color:#fff}
.services-text{left:98px;top:1470px;width:250px;font-size:15px;line-height:28px;color:#fff}
.card{width:262px;height:300px;padding:60px 36px 0;color:#fff}
.card.orange{background:var(--orange)}
.card.black{background:#262626}
.card svg{width:50px;height:50px;margin-bottom:18px}
.card h3{font-family:"Krona One",sans-serif;font-size:15px;line-height:20px;font-weight:400}
.card p{font-size:12px;line-height:19px;margin-top:12px}

/* projects */
.proj-eyebrow{left:0;width:1200px;top:1892px;justify-content:center}
.proj-title{left:0;width:1200px;top:1922px;text-align:center;font-size:30px}
.proj{color:#fff;display:flex;flex-direction:column;justify-content:flex-end;padding:0 20px 18px}
.proj h4{font-family:"Krona One",sans-serif;font-size:14px;font-weight:400}
.proj p{font-size:12px;line-height:17px;margin-top:8px}

/* quote */
.quote{left:0;top:2497px;width:1200px;height:590px;background:linear-gradient(180deg,#2a2a2a,#111)}
.quote-band{left:0;top:2870px;width:1200px;height:160px;background:var(--lime);clip-path:polygon(0 70%,100% 0,100% 35%,0 100%)}
.quote-eyebrow{left:0;width:1200px;top:2584px;justify-content:center}
.quote-title{left:0;width:1200px;top:2618px;text-align:center;color:#fff;font-size:30px}
.quote-sub{left:0;width:1200px;top:2660px;text-align:center;color:#fff;font-size:14px;line-height:22px}
.form{left:210px;top:2729px;width:491px;height:318px;background:#fff}
.field{font-size:12px;border-bottom:1px solid #ccc;padding-bottom:18px}
.submit{left:537px;top:2981px;background:#000;color:#fff;font-size:15px;font-weight:600;padding:12px 30px}
.contact{left:701px;top:2729px;width:289px;height:318px;background:var(--lime);padding:34px 46px}
.contact h4{font-family:"Krona One",sans-serif;font-size:15px;font-weight:400;line-height:22px;margin-bottom:16px}
.c-row{display:flex;gap:12px;font-size:12px;line-height:18px;margin-bottom:16px}
.c-row svg{flex:none;width:22px;height:22px}
.social{display:flex;gap:8px}
.social span{width:27px;height:27px;border:1.5px solid #111}

/* newsletter */
.news-img{left:298px;top:3152px;width:110px;height:148px;background:linear-gradient(160deg,#2d5bc3,#13317d);border-radius:14px 40px 14px 40px}
.news-title{left:455px;top:3152px;font-size:17px;color:var(--navy)}
.news-text{left:420px;top:3187px;width:480px;text-align:center;font-size:14px;line-height:21px}
.news-input{left:413px;top:3242px;width:333px;height:36px;border:1px solid #ccc;border-right:none;font-size:12px;padding:10px 12px}
.news-btn{left:746px;top:3242px;width:153px;height:36px;background:var(--lime);font-family:"Krona One",sans-serif;font-size:13px;display:flex;align-items:center;justify-content:center}

/* footer */
.rule{left:141px;top:3330px;width:917px;height:1px;background:#ddd}
.foot-brand{left:0;width:1200px;top:3420px;justify-content:center;font-size:17px}
.foot-nav{left:353px;top:3478px;display:flex;gap:38px;font-size:13px}
.foot-nav .on{color:var(--lime)}
.foot-dark{left:0;top:3558px;width:1200px;height:114px;background:#111}
.foot-bar{left:141px;top:3510px;width:917px;height:87px;background:var(--lime);display:flex;gap:40px;padding:0 0 0 180px;align-items:center}
.foot-bar .c-row{margin:0;font-size:13px}
.machine{left:935px;top:3395px;width:245px;height:160px;background:linear-gradient(135deg,#f0a038,#d97c1a 60%,#444);border-radius:30px 80px 10px 20px}
.copyright{left:141px;top:3625px;color:#fff;font-size:12px}
.foot-social{left:908px;top:3618px;display:flex;gap:10px}
.foot-social span{width:30px;height:30px;border:1.5px solid #fff}
</style>
</head>
<body>

<!-- header -->
<div class="abs topbar"></div>
<div class="abs topbar-info">
  <span>Phone: <b>(123) 456 7890 / (533) 456 1259</b></span>
  <span>Email Us On: <b>info@gullwindstonecut.example</b></span>
</div>
<div class="abs brand"><span class="brand-mark"></span>GULLWIND STONECUT EARTHWORKS</div>
<nav class="abs nav">
  <span>HOME</span><span>ABOUT US</span><span>SERVICES</span><span>OUR PROJECT</span>
  <span class="nav-cta">CONTACT US &rarr;</span>
</nav>

<!-- hero -->
<div class="abs hero" role="img" aria-label="Yellow excavator loading soil into a dump truck beside large steel pipes"></div>
<div class="abs hero-tag">PERTH, WESTERN AUSTRALIA</div>
<h1 class="abs hero-title display">Earth Moved<br>With Precision</h1>
<p class="abs hero-text">Professional excavation, bulk earthworks, site preparation and land development services across Perth and Western Australia.</p>
<div class="abs btn btn-lime">VIEW PROJECTS &rarr;</div>
<div class="abs btn btn-white">GET A QUOTE &rarr;</div>

<!-- about -->
<div class="abs about-img" role="img" aria-label="Site workers in hi-vis vests beside excavators and a dump truck"></div>
<div class="abs about-label">ABOUT US</div>
<h2 class="abs about-title display">Gullwind Stonecut<br>Earthworks</h2>
<div class="abs about-rule"></div>
<div class="abs about-text">
  <p>Gullwind Stonecut Earthworks is Perth's trusted partner for excavation and earthmoving solutions. Founded on principles of precision, reliability, and uncompromising quality, we've built our reputation one project at a time.</p>
  <p>Our team brings decades of combined experience to every job, from residential site preparation to large-scale commercial developments. We invest in the latest equipment and technology to ensure efficiency, safety, and superior results.</p>
</div>
<div class="abs btn btn-about">WORK WITH US</div>

<!-- services -->
<div class="abs services-intro" role="img" aria-label="Excavator under a stormy sky"></div>
<div class="abs eyebrow" style="left:98px;top:1357px">WHAT WE DO</div>
<h2 class="abs services-title display">Our<br>Services</h2>
<p class="abs services-text">Comprehensive earthmoving and excavation solutions for projects of all sizes across Perth and regional WA.</p>

<div class="abs card orange" style="left:413px;top:1198px">
  <svg viewBox="0 0 50 50" fill="none" stroke="#fff" stroke-width="2"><rect x="4" y="30" width="26" height="10"/><rect x="10" y="20" width="12" height="10"/><path d="M22 22 L36 8 L44 18 L40 22"/><circle cx="10" cy="44" r="3"/><circle cx="24" cy="44" r="3"/></svg>
  <h3>Bulk<br>Earthworks</h3>
  <p>Large-scale cut and fill operations, land levelling, and soil compaction for subdivisions and commercial developments.</p>
</div>
<div class="abs card black" style="left:675px;top:1198px">
  <svg viewBox="0 0 50 50" fill="none" stroke="#fff" stroke-width="2"><path d="M4 44 H46 M8 44 V24 L20 34 L26 26 L34 34"/><circle cx="38" cy="12" r="6"/></svg>
  <h3>Land<br>Clearing</h3>
  <p>Vegetation removal, stump grinding, and site preparation for residential, agricultural and commercial properties.</p>
</div>
<div class="abs card orange" style="left:937px;top:1198px">
  <svg viewBox="0 0 50 50" fill="none" stroke="#fff" stroke-width="2"><path d="M20 4 H30 L40 44 H10 Z M25 12 V18 M25 24 V30 M25 36 V42"/></svg>
  <h3>Road &amp; Driveway<br>Construction</h3>
  <p>Formation, grading and compaction for access roads, farm tracks, and residential driveways.</p>
</div>
<div class="abs card black" style="left:413px;top:1498px">
  <svg viewBox="0 0 50 50" fill="none" stroke="#fff" stroke-width="2"><rect x="6" y="6" width="26" height="38"/><path d="M32 20 C40 24 42 32 44 44"/></svg>
  <h3>Dam<br>&amp; Drainage</h3>
  <p>Dam construction, excavation, lining, and drainage solutions for flood mitigation and water management.</p>
</div>
<div class="abs card orange" style="left:675px;top:1498px">
  <svg viewBox="0 0 50 50" fill="none" stroke="#fff" stroke-width="2"><path d="M10 44 V6 M4 8 H40 M10 14 L18 8 M36 8 V16"/><rect x="24" y="26" width="16" height="18"/></svg>
  <h3>Site<br>Preparation</h3>
  <p>Complete site preparation for residential and commercial construction, including slab foundations and pad preparation.</p>
</div>
<div class="abs card black" style="left:937px;top:1498px">
  <svg viewBox="0 0 50 50" fill="none" stroke="#fff" stroke-width="2"><path d="M4 22 H30 L26 36 H8 Z"/><circle cx="12" cy="42" r="3"/><circle cx="24" cy="42" r="3"/><circle cx="38" cy="20" r="8"/></svg>
  <h3>Material<br>Supply &amp; Removal</h3>
  <p>Supply of quality fill material, sand, gravel, and removal of excess spoil from your site.</p>
</div>

<!-- projects -->
<div class="abs eyebrow center proj-eyebrow">CREATIONS</div>
<h2 class="abs proj-title display">Our Projects</h2>
<div class="abs proj" style="left:141px;top:1995px;width:286px;height:229px;background:linear-gradient(180deg,#b58a5c,#6a5034 60%,#2a2218)" role="img" aria-label="Excavator digging in a rocky quarry">
  <h4>Lorem ipsum dolorsit</h4><p>Duis autem vel eum iriure dolor in hendrerit in vulputate velit esse mole.</p></div>
<div class="abs proj" style="left:437px;top:1995px;width:286px;height:229px;background:linear-gradient(180deg,#3f5a2c,#5b5a35 60%,#22231a)" role="img" aria-label="Excavator clearing bushland">
  <h4>Lorem ipsum dolor amet</h4><p>Duis autem vel eum iriure dolor in hendrerit in vulputate velit esse mole.</p></div>
<div class="abs proj" style="left:733px;top:1995px;width:325px;height:155px;background:linear-gradient(180deg,#8e9ba2,#5d5f50 60%,#222)" role="img" aria-label="Excavator beside a house in autumn woodland">
  <h4>Lorem ipsum dolor sit amet,</h4><p>Duis autem vel eum iriure dolor in hendrerit in vulputate velit esse molestie consequat.</p></div>
<div class="abs proj" style="left:141px;top:2235px;width:581px;height:167px;background:linear-gradient(90deg,#7c8a5a,#8d8c80 40%,#4a4a44);padding-left:395px" role="img" aria-label="Aerial view of a road works crew in a suburban street">
  <h4>Lorem ipsum<br>dolor sit amet,</h4><p>Duis autem vel eum iriure dolor in hendrerit in vulputate velit esse molestie consequat.</p></div>
<div class="abs proj" style="left:733px;top:2161px;width:325px;height:241px;background:linear-gradient(180deg,#c9a16a,#7a5a36 55%,#1e1a14)" role="img" aria-label="Excavator silhouetted at sunset">
  <h4>Lorem ipsum dolor sit amet,</h4><p>Duis autem vel eum iriure dolor in hendrerit in vulputate velit esse molestie consequat.</p></div>

<!-- quote -->
<div class="abs quote" role="img" aria-label="Darkened earthworks site with tracked machinery"></div>
<div class="abs quote-band"></div>
<div class="abs eyebrow center quote-eyebrow">QUICK INQUIRY</div>
<h2 class="abs quote-title display">Request A Quote</h2>
<p class="abs quote-sub">Ready to move earth? Contact our Perth team for a no-obligation<br>site assessment and quote.</p>
<div class="abs form"></div>
<div class="abs field" style="left:235px;top:2768px;width:205px">First name*</div>
<div class="abs field" style="left:466px;top:2768px;width:203px">Last name*</div>
<div class="abs field" style="left:235px;top:2824px;width:205px">Your phone*</div>
<div class="abs field" style="left:466px;top:2824px;width:203px">Your email*</div>
<div class="abs field" style="left:235px;top:2881px;width:434px;padding-bottom:50px">Message</div>
<div class="abs submit">SUBMIT NOW</div>
<div class="abs contact">
  <h4>CONTACT<br>INFORMATION</h4>
  <div class="c-row"><svg viewBox="0 0 24 24"><path d="M12 2a7 7 0 0 0-7 7c0 5 7 13 7 13s7-8 7-13a7 7 0 0 0-7-7zm0 10a3 3 0 1 1 0-6 3 3 0 0 1 0 6z" fill="#111"/></svg><span>123, Building Name, Street<br>City, State XY 123456</span></div>
  <div class="c-row"><svg viewBox="0 0 24 24"><path d="M6 3l4 4-2 3c1 2 4 5 6 6l3-2 4 4-3 3C10 21 3 14 3 6z" fill="none" stroke="#111" stroke-width="2"/></svg><span>PHONE<br>(123) 456 7890</span></div>
  <div class="c-row"><svg viewBox="0 0 24 24"><rect x="2" y="5" width="20" height="14" fill="#111"/><path d="M2 5l10 8 10-8" stroke="#c9d32f" stroke-width="1.5" fill="none"/></svg><span>EMAIL<br>hello@gullwindstonecut.example</span></div>
  <div class="social"><span></span><span></span><span></span><span></span></div>
</div>

<!-- newsletter -->
<div class="abs news-img" role="img" aria-label="Envelope illustration holding a letter"></div>
<h3 class="abs news-title display">Subscribe To Our Newsletter</h3>
<p class="abs news-text">Want to keep up to date with all our latest news and information?<br>Enter your email below to be added to our mailing list.</p>
<div class="abs news-input">Enter your email address</div>
<div class="abs news-btn">SUBSCRIBE</div>

<!-- footer -->
<div class="abs rule"></div>
<div class="abs brand foot-brand"><span class="brand-mark"></span>GULLWIND STONECUT EARTHWORKS</div>
<nav class="abs foot-nav"><span class="on">HOME</span><span>ABOUT US</span><span>SERVICES</span><span>PROJECTS</span><span>CONTACT US</span></nav>
<div class="abs foot-dark"></div>
<div class="abs foot-bar">
  <div class="c-row"><svg viewBox="0 0 24 24" width="22" height="22"><path d="M12 2a7 7 0 0 0-7 7c0 5 7 13 7 13s7-8 7-13a7 7 0 0 0-7-7zm0 10a3 3 0 1 1 0-6 3 3 0 0 1 0 6z" fill="#111"/></svg><span>123, Building Name, Street<br>City, State XY 123456</span></div>
  <div class="c-row"><svg viewBox="0 0 24 24" width="22" height="22"><path d="M6 3l4 4-2 3c1 2 4 5 6 6l3-2 4 4-3 3C10 21 3 14 3 6z" fill="none" stroke="#111" stroke-width="2"/></svg><span>PHONE<br>(123) 456 7890</span></div>
  <div class="c-row"><svg viewBox="0 0 24 24" width="22" height="22"><rect x="2" y="5" width="20" height="14" fill="#111"/><path d="M2 5l10 8 10-8" stroke="#c9d32f" stroke-width="1.5" fill="none"/></svg><span>EMAIL<br>hello@gullwindstonecut.example</span></div>
</div>
<div class="abs machine" role="img" aria-label="Orange tracked excavator cut-out"></div>
<div class="abs copyright">© 2026 Gullwind Stonecut Earthworks. All Rights Reserved.</div>
<div class="abs foot-social"><span></span><span></span><span></span><span></span></div>

</body>
</html>
```